Simple Modern Label for a Coconut oil product

We need a label designed for Organic Coconut oil. We would like the label to convey the gourmet/high quality product. It should be modern and simple and look like an artisinal product. The label will need to contain all the basic label requirements - Independence list, place for nutrition facts, our company logo etc.
The label will ultimately be printed as oil proof, so it will have a glossy appearance.
I have includes some examples that I like and a file with the logo.

Product Container - Wide Mount Clear Glass Jar: 4.75 inches tall (base to the bottom of the lid) and 9.5 in circumference
Label: Can be 1 or 2 separate labels, round, square and rectangle are okay
No larger than 3 inches high and 9 inches long

Target Market(s)

Middle Age home chef

Industry/Entity Type

Product

Requirements
Must have
• - logo (Attached below, I have this in multiple formats, let me know if you need them)
• - 14 FL OZ (414mL)
• - ingredient: organic unrefined whole kernel virgin coconut oil,
• - Manufacturer: XXX Y St., anywhere, CA, 99999
• - Distributed by Fernvale Naturals, P.O. Box 5521, Oakland, CA 94610 www.FernvaleNaturals.example
• - Certified Organic by Company Name
• - Product of Sri Lanka
Nice to have
• - Nutrition Facts
Should not have
• Clutter

```html
<!DOCTYPE html>
<html lang="en">
<head>
<meta charset="utf-8">
<title>Fernvale Naturals Organic Coconut Oil Label</title>
<link rel="stylesheet" href="https://fonts.googleapis.com/css2?family=Montserrat:wght@500;600&family=Pinyon+Script&family=Playfair+Display:wght@700;900&family=Arimo:wght@400&display=swap">
<style>
  :root {
    --page: #efefef;
    --label: #ffffff;
    --navy: #1d3566;
    --ink: #1c1c1c;
    --ink-soft: #555555;
    --magenta: #b8307e;
    --magenta-light: #cf4a96;
    --aqua: #cfe9ec;
    --rule: #3a3a3a;
  }
  * { box-sizing: border-box; margin: 0; padding: 0; }
  html, body {
    width: 1200px; height: 896px; overflow: hidden;
    background: var(--page);
  }
  .canvas {
    position: relative; width: 1200px; height: 896px;
    display: flex; align-items: center; justify-content: center;
  }
  .label {
    position: relative; width: 900px; height: 560px;
    background: var(--label);
    overflow: hidden;
    box-shadow: 0 2px 10px rgba(0,0,0,0.08);
  }
  .brand {
    position: absolute; top: 58px; left: 0; right: 0;
    display: flex; align-items: center; justify-content: center; gap: 14px;
  }
  .brand-square {
    width: 46px; height: 46px; background: var(--navy);
  }
  .brand-name {
    font-family: "Montserrat", sans-serif; font-weight: 600;
    font-size: 34px; letter-spacing: 2px; color: var(--navy);
    text-transform: uppercase;
  }
  .product-kind {
    position: absolute; top: 150px; left: 0; right: 0; text-align: center;
    font-family: "Pinyon Script", cursive; font-size: 46px; color: var(--ink-soft);
    margin-left: -150px;
  }
  .product-name {
    position: absolute; top: 196px; left: 0; right: 0; text-align: center;
    font-family: "Playfair Display", serif; font-weight: 900;
    font-size: 118px; line-height: 1; letter-spacing: 2px; color: var(--ink);
    text-shadow: 4px 4px 0 #c9c9c9;
  }
  .product-sub {
    position: absolute; top: 322px; left: 0; right: 0;
    display: flex; align-items: center; justify-content: center; gap: 18px;
  }
  .product-sub .rule { width: 150px; height: 2px; background: var(--rule); }
  .product-sub .word {
    font-family: "Playfair Display", serif; font-weight: 700;
    font-size: 54px; line-height: 1; color: var(--ink); letter-spacing: 3px;
  }
  .base-band {
    position: absolute; left: 0; right: 0; top: 425px; bottom: 0;
    background: var(--aqua);
  }
  .claims {
    position: absolute; left: 30px; right: 30px; top: 395px; height: 62px;
    border-radius: 8px;
    background: linear-gradient(180deg, var(--magenta-light), var(--magenta));
    display: flex; align-items: center; justify-content: center; gap: 22px;
    font-family: "Montserrat", sans-serif; font-weight: 500;
    font-size: 25px; letter-spacing: 4px; color: #ffffff;
  }
  .net-content {
    position: absolute; left: 0; right: 0; top: 492px; text-align: center;
    font-family: "Arimo", sans-serif; font-size: 26px; color: var(--ink);
  }
</style>
</head>
<body>
  <main class="canvas">
    <section class="label">
      <div class="brand">
        <span class="brand-square"></span>
        <span class="brand-name">Fernvale Naturals</span>
      </div>
      <p class="product-kind">Organic</p>
      <h1 class="product-name">COCONUT</h1>
      <div class="product-sub">
        <span class="rule"></span>
        <span class="word">OIL</span>
        <span class="rule"></span>
      </div>
      <div class="base-band"></div>
      <div class="claims">
        <span>UNREFINED</span><span>|</span><span>EXTRAVIRGIN</span><span>|</span><span>RAW</span>
      </div>
      <p class="net-content">14 FL OZ (414mL)</p>
    </section>
  </main>
</body>
</html>
```